Van Sign Writing for Electrical & Security Systems Compay

We are an Electrical, Intruder Alarm / CCTV and Automation company. We would like a design to have our van Sign Written. The van is a 2021 Velmont corvane. We DON'T want to completely wrap it, just work with the colour of the van and the logo and wording provided. Although we are open to some unique designs to complement the logo and wording. Pictures of the van front, side and back have been provided along with the logo.

Please use fake placeholders for the Phone Number Email Address and Web Address, these will be provided later.

The Servies that need to be displayed are:

Electrical
Intruder Alarms & CCTV
Access Control
EV Chargers
Home Automation
Fire Alarms
Fire Protection

The social media Icons that need to be displayed are:
Lunemark
Quellorix
Bravitel
Marquine
Dovlette
There needs to be space under these icons for a web address. The exact van colour is VELMONT PAINT KPW GRIS URBAN. The image also attached of colour.

Target Market(s)

Electrical
Intruder Alarms & CCTV
Access Control
EV Chargers
Home Automation
Fire Alarms
Fire Protection

Requirements
Must have
• As per Description
Nice to have
• Unique design to compliment text, logo and colours
Should not have
• Full wrap

```html
<!DOCTYPE html>
<html lang="en">
<head>
<meta charset="utf-8">
<title>Kavren – Van Livery Layout</title>
<link rel="stylesheet" href="https://fonts.googleapis.com/css2?family=Montserrat:wght@600;700;800&display=swap">
<style>
  :root{
    --paint:#8fc3ca;
    --accent:#6ccbdb;
    --band:#2b2f31;
    --ink:#253538;
    --white:#ffffff;
    --stage:#ecedee;
    --gap:#ffffff;
    --plate:#d9dcdd;
  }
  html,body{margin:0;padding:0;overflow:hidden;}
  body{width:1200px;height:801px;background:var(--gap);font-family:"Montserrat",sans-serif;}
  .sheet{position:relative;width:1200px;height:801px;}
  .view{position:absolute;background:var(--stage);overflow:hidden;}
  .view svg{display:block;width:100%;height:100%;}
  .view--side-left{left:0;top:0;width:796px;height:398px;}
  .view--rear{left:800px;top:0;width:400px;height:398px;}
  .view--side-right{left:0;top:402px;width:796px;height:399px;}
  .view--front{left:800px;top:402px;width:400px;height:399px;}
  .paint{fill:var(--paint);}
  .band{fill:var(--band);}
  .mark{fill:none;stroke:var(--accent);stroke-width:9;}
  .mark--white{fill:none;stroke:var(--white);stroke-width:6;}
  .brand{font-family:"Montserrat",sans-serif;font-weight:800;fill:var(--accent);}
  .brand--white{fill:var(--white);}
  .tagline{font-family:"Montserrat",sans-serif;font-weight:700;fill:var(--white);letter-spacing:4px;}
  .phone{font-family:"Montserrat",sans-serif;font-weight:700;fill:var(--band);}
  .phone--white{fill:var(--white);}
  .services{font-family:"Montserrat",sans-serif;font-weight:700;fill:var(--ink);}
  .web{font-family:"Montserrat",sans-serif;font-weight:800;fill:var(--accent);}
  .web--white{fill:var(--white);letter-spacing:3px;}
  .socials{font-family:"Montserrat",sans-serif;font-weight:700;fill:var(--ink);}
  .email{font-family:"Montserrat",sans-serif;font-weight:600;fill:var(--white);letter-spacing:1.5px;}
  .plate{fill:var(--plate);}
  .plate-label{font-family:"Montserrat",sans-serif;font-weight:800;fill:var(--band);}
</style>
</head>
<body>
<main class="sheet">

  <section class="view view--side-left" aria-label="Nearside livery layout">
    <svg viewBox="0 0 796 398">
      <rect class="paint" x="30" y="40" width="736" height="320" rx="30"/>
      <polygon class="band" points="30,250 766,110 766,230 30,360"/>
      <g transform="translate(390 172) rotate(-11)">
        <text class="services" x="40" y="-36" font-size="12">• Electrical • Intruder Alarms &amp; CCTV</text>
        <text class="services" x="0" y="-20" font-size="12">• Access Control • EV Chargers • Home Automation</text>
        <text class="services" x="70" y="-4" font-size="12">• Fire Alarms • Fire Protection</text>
      </g>
      <g transform="translate(430 190) rotate(-11)">
        <text class="brand" x="0" y="58" font-size="66">KAVREN</text>
        <text class="tagline" x="8" y="86" font-size="20">GET CONNECTED</text>
        <text class="phone" x="0" y="132" font-size="32">+0198 765 4321</text>
        <text class="socials" x="4" y="156" font-size="11">Bravitel · Lunemark · Quellorix · Dovlette · Marquine</text>
      </g>
      <circle class="mark" cx="355" cy="250" r="55"/>
      <g transform="translate(170 320) rotate(-11)">
        <text class="web" x="0" y="0" font-size="20">kavren.com</text>
      </g>
    </svg>
  </section>

  <section class="view view--rear" aria-label="Rear door livery layout">
    <svg viewBox="0 0 400 398">
      <rect class="band" x="45" y="50" width="310" height="320" rx="14"/>
      <rect class="paint" x="60" y="48" width="280" height="300" rx="8"/>
      <circle class="mark--white" cx="112" cy="120" r="34"/>
      <text class="brand brand--white" x="156" y="118" font-size="34">KAVREN</text>
      <text class="tagline" x="158" y="133" font-size="10" letter-spacing="2">GET CONNECTED</text>
      <rect class="band" x="150" y="140" width="176" height="28"/>
      <text class="phone phone--white" x="158" y="162" font-size="22">198 765 4321</text>
      <text class="email" x="103" y="184" font-size="8">kavrenconnect@mailbox.com</text>
      <text class="web web--white" x="80" y="204" font-size="16">www.kavren.com</text>
      <rect class="plate" x="88" y="268" width="98" height="20"/>
      <text class="plate-label" x="101" y="283" font-size="11">VELMONT</text>
    </svg>
  </section>

  <section class="view view--side-right" aria-label="Offside livery layout">
    <svg viewBox="0 0 796 399">
      <rect class="paint" x="30" y="40" width="736" height="320" rx="30"/>
      <polygon class="band" points="30,110 766,250 766,360 30,230"/>
      <g transform="translate(80 72) rotate(11)">
        <text class="services" x="40" y="0" font-size="12">• Electrical • Intruder Alarms &amp; CCTV</text>
        <text class="services" x="0" y="16" font-size="12">• Access Control • EV Chargers • Home Automation</text>
        <text class="services" x="70" y="32" font-size="12">• Fire Alarms • Fire Protection</text>
      </g>
      <g transform="translate(90 137) rotate(11)">
        <text class="brand" x="0" y="58" font-size="66">KAVREN</text>
        <text class="tagline" x="8" y="86" font-size="20">GET CONNECTED</text>
        <text class="phone" x="0" y="132" font-size="32">+0198 765 4321</text>
        <text class="socials" x="4" y="156" font-size="11">Bravitel · Lunemark · Quellorix · Dovlette · Marquine</text>
      </g>
      <circle class="mark" cx="520" cy="255" r="60"/>
      <g transform="translate(610 285) rotate(11)">
        <text class="web" x="0" y="0" font-size="20">kavren.com</text>
      </g>
    </svg>
  </section>

  <section class="view view--front" aria-label="Bonnet livery layout">
    <svg viewBox="0 0 400 399">
      <rect class="band" x="40" y="60" width="320" height="310" rx="26"/>
      <rect class="paint" x="58" y="40" width="284" height="200" rx="24"/>
      <circle class="mark--white" cx="130" cy="170" r="26"/>
      <text class="brand brand--white" x="165" y="170" font-size="30">KAVREN</text>
      <text class="tagline" x="167" y="184" font-size="8" letter-spacing="2">GET CONNECTED</text>
      <rect class="plate" x="145" y="330" width="110" height="26" rx="3"/>
    </svg>
  </section>

</main>
</body>
</html>
```